Book Cover Design

Design with title UNWAVERING
Subtitle: Ways to Kindle the Spark of Resolve
Author Name: Carla Jean Morrow
Put DAILY MERIDIAN BESTSELLER at top
Shimmer design, see inspirational images attached

```html
<!DOCTYPE html>
<html lang="en">
<head>
<meta charset="utf-8">
<title>Unwavering – Book Cover</title>
<link rel="stylesheet" href="https://fonts.googleapis.com/css2?family=Bebas+Neue&family=Montserrat:wght@300;400;500&display=swap">
<style>
  :root {
    --backdrop: #d3d4d6;
    --foil-lilac: #b9a9dc;
    --foil-periwinkle: #8c9bd6;
    --foil-pink: #f6dbea;
    --foil-sky: #bfe6f8;
    --foil-white: #f4f0f8;
    --badge-ink: #4a55a8;
    --subtitle-ink: #111111;
    --author-ink: #1a75bc;
  }
  * { margin: 0; padding: 0; box-sizing: border-box; }
  html, body {
    width: 1200px;
    height: 1200px;
    overflow: hidden;
    background: var(--backdrop);
  }
  .canvas {
    position: relative;
    width: 1200px;
    height: 1200px;
    background: var(--backdrop);
  }
  .book-cover {
    position: absolute;
    left: 240px;
    top: 60px;
    width: 720px;
    height: 1080px;
    overflow: hidden;
    background:
      radial-gradient(ellipse 260px 200px at 560px 120px, var(--foil-white) 0%, rgba(246,219,234,0.7) 40%, rgba(246,219,234,0) 100%),
      radial-gradient(ellipse 260px 220px at 220px 420px, rgba(250,225,238,0.95) 0%, rgba(246,219,234,0) 100%),
      radial-gradient(ellipse 300px 260px at 580px 800px, rgba(191,230,248,0.95) 0%, rgba(191,230,248,0) 100%),
      radial-gradient(ellipse 260px 300px at 60px 120px, rgba(130,150,210,0.9) 0%, rgba(130,150,210,0) 100%),
      radial-gradient(ellipse 320px 240px at 260px 900px, rgba(140,155,214,0.9) 0%, rgba(140,155,214,0) 100%),
      radial-gradient(ellipse 200px 260px at 700px 400px, rgba(140,155,214,0.8) 0%, rgba(140,155,214,0) 100%),
      radial-gradient(ellipse 220px 180px at 60px 650px, rgba(200,180,225,0.9) 0%, rgba(200,180,225,0) 100%),
      radial-gradient(ellipse 200px 160px at 650px 1040px, rgba(230,240,250,0.9) 0%, rgba(230,240,250,0) 100%),
      linear-gradient(160deg, var(--foil-periwinkle) 0%, var(--foil-lilac) 45%, var(--foil-sky) 100%);
  }
  .bestseller-badge {
    position: absolute;
    top: 117px;
    left: 0;
    width: 100%;
    text-align: center;
    font-family: "Montserrat", sans-serif;
    font-weight: 400;
    font-size: 29px;
    letter-spacing: 0.2px;
    color: var(--badge-ink);
  }
  .book-title {
    position: absolute;
    left: 50px;
    top: 480px;
    width: 630px;
    height: 180px;
  }
  .book-title text {
    font-family: "Bebas Neue", sans-serif;
    font-size: 206px;
  }
  .book-subtitle {
    position: absolute;
    top: 686px;
    left: 0;
    width: 100%;
    text-align: center;
    font-family: "Montserrat", sans-serif;
    font-weight: 400;
    font-size: 27px;
    color: var(--subtitle-ink);
    text-transform: uppercase;
    letter-spacing: -0.3px;
  }
  .book-author {
    position: absolute;
    top: 1028px;
    left: 0;
    width: 100%;
    text-align: center;
    font-family: "Montserrat", sans-serif;
    font-weight: 500;
    font-size: 44px;
    color: var(--author-ink);
    letter-spacing: -0.5px;
    text-transform: uppercase;
    top: 1030px;
  }
  .book-cover .book-author { top: 970px; }
</style>
</head>
<body>
  <div class="canvas">
    <div class="book-cover">
      <p class="bestseller-badge">DAILY MERIDIAN BESTSELLER</p>

      <svg class="book-title" viewBox="0 0 630 180" role="img" aria-label="Unwavering">
        <defs>
          <linearGradient id="titleFoil" x1="0" y1="0" x2="1" y2="0">
            <stop offset="0" stop-color="#7c4aa6" stop-opacity="0.85"/>
            <stop offset="0.25" stop-color="#e79cc6" stop-opacity="0.75"/>
            <stop offset="0.5" stop-color="#9f7ccf" stop-opacity="0.8"/>
            <stop offset="0.75" stop-color="#6b6fc2" stop-opacity="0.85"/>
            <stop offset="1" stop-color="#3f4fa8" stop-opacity="0.95"/>
          </linearGradient>
        </defs>
        <text x="0" y="162" textLength="630" lengthAdjust="spacingAndGlyphs" fill="url(#titleFoil)">UNWAVERING</text>
      </svg>

      <p class="book-subtitle">Ways to Kindle the Spark of Resolve</p>

      <p class="book-author">Carla Jean Morrow</p>
    </div>
  </div>
</body>
</html>
```